依頼詳細
・ダイエットコース参加者を募集するためにTAVO公式アカウントご登録者募集のランディングページのヘッダーデザインをお願いします。
記載項目
キャッチコピー
・人生最後のダイエットにしたい方へ
・成功率98%
・3ヶ月で最大ー9kg!
・実績数,2000人越え
・しっかり食べれば簡単に痩せていく
一生リバウンドしない体になる食べ痩せエクササイズ

※変わる可能性がありますので、文字修正は簡単にできるようにお願い致します。
サイズ
• 横1300 × 縦957
希望イメージ
シンプル 複雑
単色 カラフル
暗い 明るい
日常 高級
遊び心 厳粛
未来的 伝統的
女性的 男性的
希望する色
シャンパンゴールドとピンクを基本にエレガントな色味でお願いします。
納品ファイル
• PNG形式 (.png)
補足説明
・女性ファッション誌のようなスタイリッシュなデザインを希望します。
・40代から60代前半の女性が対象となります。
・女性がメインなので、優しいシャンパンゴールドとピンクを基調としてお願い致します。
・イメージ写真を参考にして下さい。
・添付している開脚の写真を入れて下さい。

・当LPを閲覧する人の80%程度はスマホでの閲覧と想定されます。
スマホで閲覧しても、PCからの閲覧でも、どちらでもきれいに表示されるように
お願いいたします。
・サイズは横1300×縦957でお願いします。
・写真のイメージ重視なので、文字のインパクトよりも、
全体的に女子が好きそうな感じでお願いします。
■ 選んだ理由

3日間のキャンペーンで、TAVO公式へたくさんの女性にご登録いただきたいので、
① パッと見た時のインパクト(キャッチコピーや開脚画像が目立つかどうか)
② ターゲットが美意識の高い40代以上の女性なので、オシャレだけど洗練されすぎず

という観点で選ばせていただきました。

私が参加している集客塾の塾長と一緒に選定させていただきまして、意見がピッタリ一致しました。

■ 提案者全員のお礼・コメント

皆さま、素晴らしいデザインのご提案、ありがとうございました。
ステキな作品がたくさんあり、一点に絞るのがとても難しく、正直とても迷いました。

私は定期的にTAVO公式キャンペーンを行っており、次回は8月頃を予定しております。
次回もピクトーラで発注させていただきますので、またどうぞよろしくお願いいたします。

```html
<!DOCTYPE html>
<html lang="ja">
<head>
<meta charset="UTF-8">
<title>人生最後のダイエットにしたい方へ</title>
<link href="https://fonts.googleapis.com/css2?family=Noto+Sans+JP:wght@500;700;900&family=Noto+Serif+JP:wght@700;900&display=swap" rel="stylesheet">
<style>
  :root {
    --page-pink: #f0c3cb;
    --panel-pink: #f3a9b7;
    --panel-light: #fdf0f2;
    --frame-white: #ffffff;
    --gold-light: #f3dc95;
    --gold-mid: #c7a24a;
    --gold-dark: #8c6a22;
    --rose-red: #d9223f;
    --ink: #2a2226;
    --photo-light: #f1d6cc;
    --photo-mid: #d9b3a6;
  }
  * { margin: 0; padding: 0; box-sizing: border-box; }
  html, body { width: 1200px; height: 883px; overflow: hidden; }
  body {
    background: var(--page-pink);
    font-family: "Noto Sans JP", sans-serif;
    color: var(--ink);
    position: relative;
  }
  .hero-panel {
    position: absolute;
    left: 30px; top: 24px;
    width: 1140px; height: 564px;
    border: 8px solid var(--frame-white);
    border-radius: 22px;
    background: radial-gradient(ellipse at 48% 45%, var(--panel-light) 0%, #f8cfd7 38%, var(--panel-pink) 100%);
    box-shadow: 0 4px 12px rgba(180, 90, 110, 0.25);
  }
  .hero-photo {
    position: absolute;
    left: 108px; top: 340px;
    width: 1040px; height: 310px;
    border-radius: 120px;
    background: radial-gradient(ellipse at 50% 45%, var(--photo-light) 0%, var(--photo-mid) 70%, rgba(217,179,166,0.6) 100%);
  }
  .gold-text {
    background: linear-gradient(180deg, var(--gold-light) 0%, var(--gold-mid) 50%, var(--gold-dark) 100%);
    -webkit-background-clip: text;
    background-clip: text;
    color: transparent;
    filter: drop-shadow(2px 3px 0 rgba(255,255,255,0.9)) drop-shadow(0 2px 3px rgba(120,70,30,0.35));
  }
  .headline {
    position: absolute;
    left: 0; top: 0;
    font-weight: 900;
    white-space: nowrap;
  }
  .headline-line {
    position: absolute;
    display: block;
    transform: rotate(-10deg);
    transform-origin: left bottom;
  }
  .headline-top {
    left: 50px; top: 96px;
    font-family: "Noto Serif JP", serif;
    font-size: 124px; line-height: 1;
  }
  .headline-top .particle { font-size: 62px; }
  .headline-bottom {
    left: 96px; top: 248px;
    line-height: 1;
  }
  .headline-bottom .keyword {
    display: inline-block;
    font-size: 86px;
    letter-spacing: -2px;
    color: var(--rose-red);
    transform: skewX(-8deg);
    text-shadow: 3px 3px 0 #fff, 0 4px 6px rgba(120, 10, 30, 0.3);
  }
  .headline-bottom .tail {
    font-family: "Noto Serif JP", serif;
    font-size: 44px;
    margin-left: 6px;
  }
  .speech-bubble {
    position: absolute;
    left: 640px; top: 282px;
    width: 536px; height: 206px;
  }
  .speech-text {
    position: absolute;
    left: 680px; top: 306px;
    width: 470px;
    text-align: center;
    transform: skewX(-10deg);
    font-weight: 700;
    line-height: 1.3;
  }
  .speech-text .line { display: block; font-size: 25px; }
  .speech-text .emphasis { font-size: 37px; color: var(--rose-red); font-weight: 900; line-height: 1.25; }
  .stats {
    position: absolute;
    left: 30px; top: 690px;
    width: 1140px;
    display: flex;
    justify-content: space-between;
  }
  .stat-card {
    width: 366px; height: 162px;
    border: 7px solid var(--frame-white);
    border-radius: 20px;
    background: radial-gradient(ellipse at 50% 50%, #ffffff 30%, #fbe0e5 65%, #f3a9b7 100%);
    box-shadow: 0 3px 8px rgba(180, 90, 110, 0.25);
    display: flex;
    align-items: center;
    justify-content: center;
    text-align: center;
    font-weight: 900;
  }
  .stat-number {
    font-family: "Noto Serif JP", serif;
    font-weight: 900;
    display: inline-block;
    transform: skewX(-12deg);
  }
  .stat-period { text-align: left; line-height: 1.15; font-size: 34px; }
  .stat-period .stat-number { font-size: 56px; }
  .stat-rate { font-size: 34px; }
  .stat-rate .stat-number { font-size: 76px; margin-left: 10px; }
  .stat-rate .unit { font-size: 44px; }
  .stat-count { line-height: 1.15; }
  .stat-count .stat-label { font-size: 36px; }
  .stat-count .stat-number { font-size: 58px; }
  .stat-count .unit { font-size: 40px; }
</style>
</head>
<body>
  <section class="hero-panel" aria-label="ヘッダー"></section>

  <div class="hero-photo" role="img" aria-label="笑顔で開脚する女性インストラクターの写真"></div>

  <h1 class="headline">
    <span class="headline-line headline-top gold-text">人生最後<span class="particle">の</span></span>
    <span class="headline-line headline-bottom"><span class="keyword">ダイエット</span><span class="tail gold-text">にしたい方へ</span></span>
  </h1>

  <svg class="speech-bubble" viewBox="0 0 536 206" aria-hidden="true">
    <path d="M14 170 L70 128 A250 98 0 1 1 92 150 Z" fill="#ffffff" opacity="0.95"/>
  </svg>
  <p class="speech-text">
    <span class="line">しっかり食べれば簡単に痩せていく</span>
    <span class="line emphasis">一生リバウンドしない</span>
    <span class="line">体になる食べ痩せエクササイズ</span>
  </p>

  <div class="stats">
    <div class="stat-card">
      <p class="stat-period"><span class="stat-number gold-text">3</span>ヶ月で<br>最大ー9kg！</p>
    </div>
    <div class="stat-card">
      <p class="stat-rate">成功率<span class="stat-number gold-text">98<span class="unit">%</span></span></p>
    </div>
    <div class="stat-card">
      <p class="stat-count"><span class="stat-label">実績数</span><br><span class="stat-number gold-text">2000</span><span class="unit gold-text">人</span><span class="stat-label"> 越え</span></p>
    </div>
  </div>
</body>
</html>
```